Website needed for Entertainment Company [Wordpress & Mobile Site] (Contest)

"Vault Learning" does Acrobatic Educational Shows for schools.
We need a 4-Page Wordpress site, for BOTH Desktop & Mobile
THINGS WE'D LIKE ON THE HOME PAGE
- Book Now buttons
- Panel advertising "Kindness-First Tumbling Tour" with subheading "Educating the Victim, Empowering the Bystander, and Enlightening the Bully" with Photo & 'Read More'
- text somewhere saying "Vault Learning engages children in important topics, by utilising Parkour & Acrobatics to captivate and enthrall todays youngest generation."
- Panel advertising Teachers Resources: "Curriculum based resources for teachers including lesson plans, workbooks, and physical activities for before & after the show." Maybe even some boxes that say a subject that is covered (eg. Mathematics. Science. PD/H/PE.)
- Everything else that you recommend
4 PAGES:
- Home Page
- About Us
- Our Program & Shows
- Teachers Resources Portal
NOTE: Transparent & Source files for logo will be provided soon (recently finished being designed)

```html
<!DOCTYPE html>
<html lang="en">
<head>
<meta charset="utf-8">
<title>Vault Learning — Home</title>
<link href="https://fonts.googleapis.com/css2?family=Oswald:wght@400;500;600;700&family=Open+Sans:ital,wght@0,400;0,600;0,700;1,600&display=swap" rel="stylesheet">
<style>
:root{
  --orange:#f5a623;
  --ink:#222326;
  --text:#55585e;
  --muted:#8a8d93;
  --slate:#3d4b5d;
  --night:#17181b;
  --paper:#ffffff;
  --mist:#f1f2f4;
  --line:#dcdee2;
}
*{box-sizing:border-box;margin:0;padding:0}
html,body{width:1200px;height:2256px;overflow:hidden}
body{font-family:"Open Sans",Arial,sans-serif;color:var(--text);background:var(--paper);position:relative}
h1,h2,h3,h4,.brand,.nav a,.btn{font-family:"Oswald","Arial Narrow",sans-serif}
.btn{display:inline-block;background:var(--orange);color:#fff;font-size:13px;font-weight:600;letter-spacing:1px;text-transform:uppercase;padding:10px 24px;border-radius:3px;text-decoration:none;white-space:nowrap}
.photo{display:block}

/* header */
.site-header{position:absolute;top:0;left:0;width:1200px;height:88px;display:flex;align-items:center;padding:0 180px;background:#fff;z-index:2}
.brand{display:flex;align-items:center;gap:8px;font-size:24px;font-weight:700;color:var(--orange);text-transform:uppercase;letter-spacing:.5px}
.brand-dot{width:14px;height:14px;border-radius:50%;background:var(--orange)}
.nav{display:flex;gap:34px;margin-left:120px}
.nav a{font-size:12px;letter-spacing:1.2px;text-transform:uppercase;color:var(--ink);text-decoration:none;padding-bottom:6px}
.nav a.active{border-bottom:2px solid var(--orange)}
.site-header .btn{margin-left:auto}

/* hero */
.hero{position:absolute;top:88px;left:0;width:1200px;height:380px}
.hero-shelf{position:absolute;right:0;top:0;width:420px;height:380px;background:linear-gradient(135deg,#a9795a,#6f4a35 60%,#3e2a1f)}
.hero-stage{position:absolute;left:600px;top:0;width:260px;height:380px;background:linear-gradient(180deg,#1d1d20,#2e2a2c)}
.hero-copy{position:absolute;left:180px;top:70px;width:400px}
.hero-copy h1{font-size:44px;line-height:1.05;color:var(--ink);font-weight:700;text-transform:uppercase}
.hero-copy h1 em{font-style:normal;text-transform:none;font-weight:600}
.hero-copy p{font-size:12px;margin:12px 0 24px;color:var(--muted)}
.hero-phone{position:absolute;left:180px;top:330px;font-size:11px;color:var(--text);display:flex;align-items:center;gap:6px}
.slider-dots{position:absolute;left:760px;top:340px;display:flex;gap:12px;color:#c9cbd0;font-size:14px}

/* feature */
.feature{position:absolute;top:490px;left:0;width:1200px;height:340px}
.feature-photo{position:absolute;left:220px;top:10px;width:252px;height:300px;background:linear-gradient(160deg,#d8dde2,#8fa5b6 70%,#f5a623)}
.feature-copy{position:absolute;left:580px;top:30px;width:420px}
.feature-copy h2{font-size:34px;line-height:1.1;letter-spacing:2px;color:var(--ink);text-transform:uppercase;font-weight:600}
.feature-copy h3{font-family:"Open Sans",sans-serif;font-size:15px;font-weight:600;color:var(--ink);margin:16px 0 10px;line-height:1.4}
.feature-copy p{font-size:12px;line-height:1.6;color:var(--muted)}
.feature-rule{width:40px;height:3px;background:var(--orange);margin-top:18px}

/* programs band */
.programs{position:absolute;top:852px;left:0;width:1200px;height:248px;background:var(--slate)}
.programs h4{position:absolute;left:220px;top:26px;color:#fff;font-size:12px;letter-spacing:1.5px;font-weight:500}
.programs .arrows{position:absolute;right:220px;top:22px;color:#fff;font-size:16px;letter-spacing:12px}
.cards{position:absolute;left:220px;top:60px;display:flex;gap:14px}
.card{width:180px;height:150px;position:relative}
.card .photo{width:180px;height:150px}
.card span{position:absolute;left:0;right:0;bottom:14px;text-align:center;font-family:"Oswald",sans-serif;font-size:13px;letter-spacing:1px;color:#fff;font-weight:500;text-transform:uppercase}

/* quote */
.quote{position:absolute;top:1118px;left:0;width:1200px;height:124px;background:var(--mist);display:flex;align-items:center;justify-content:center}
.quote p{width:760px;text-align:center;font-size:19px;font-style:italic;font-weight:600;color:var(--ink);line-height:1.5}

/* heroes */
.heroes{position:absolute;top:1262px;left:0;width:1200px;height:400px}
.heroes-photo{position:absolute;left:232px;top:2px;width:170px;height:300px;background:linear-gradient(180deg,#2d8fd0,#1c6fae)}
.heroes-nav{position:absolute;left:420px;top:346px;font-size:13px;color:var(--muted);letter-spacing:6px}
.heroes-copy{position:absolute;left:520px;top:4px;width:430px}
.heroes-copy h2{font-size:30px;line-height:1.2;letter-spacing:2px;color:var(--ink);font-weight:600;text-transform:uppercase;white-space:nowrap}
.heroes-copy .name{font-family:"Oswald",sans-serif;font-size:12px;letter-spacing:1.5px;color:var(--text);margin:4px 0 8px;text-transform:uppercase}
.heroes-copy .intro{font-size:11px;line-height:1.6;color:var(--muted);margin-bottom:10px}
.info-box{background:var(--mist);padding:12px 18px;width:390px}
.info-box h5{font-family:"Oswald",sans-serif;font-size:11px;letter-spacing:1px;color:var(--orange);font-weight:600;text-transform:uppercase}
.info-box p{font-size:11px;line-height:1.5;color:var(--text);margin:2px 0 8px;padding-bottom:7px;border-bottom:1px solid var(--line)}
.info-box p:last-child{border:0;margin-bottom:0;padding-bottom:0}
.heroes-copy .btn{margin-top:14px;font-size:11px;padding:8px 20px}

/* how we work */
.how{position:absolute;top:1680px;left:0;width:1200px;height:262px;background:linear-gradient(90deg,var(--night),#2a2b2f 60%,#3a3b40)}
.how-kid{position:absolute;right:150px;top:-26px;width:240px;height:288px;background:linear-gradient(180deg,#e9c9a0,#8a5a3c 55%,#2c2f3a)}
.how h2{position:absolute;left:220px;top:30px;color:#fff;font-size:40px;letter-spacing:3px;font-weight:600}
.how .lead{position:absolute;left:220px;top:92px;width:500px;font-size:11px;color:#b5b8bd;line-height:1.6}
.how ul{position:absolute;left:220px;top:146px;width:540px;list-style:none;display:grid;grid-template-columns:repeat(3,1fr);row-gap:14px}
.how li{font-size:11px;color:#fff;display:flex;align-items:center;gap:8px}
.how li::before{content:"";width:8px;height:8px;background:var(--orange);border-radius:2px;flex:none}

/* newsletter */
.newsletter{position:absolute;top:1972px;left:0;width:1200px;height:56px;display:flex;align-items:center;padding:0 220px;border-bottom:1px solid var(--line)}
.newsletter .field{width:440px;height:28px;border:1px solid var(--line);border-radius:3px;font-size:11px;color:var(--muted);display:flex;align-items:center;padding-left:12px;gap:8px}
.newsletter .btn{margin-left:auto;font-size:11px;padding:7px 20px}

/* footer */
.site-footer{position:absolute;top:2030px;left:0;width:1200px;height:196px;background:var(--mist)}
.footer-about{position:absolute;left:180px;top:28px;width:260px}
.footer-about p{font-size:10px;line-height:1.6;color:var(--muted);margin-top:10px}
.socials{display:flex;gap:6px;margin-top:10px}
.socials span{width:18px;height:18px;border-radius:50%;background:var(--slate)}
.enquiry{position:absolute;left:464px;top:30px;width:560px}
.enquiry h3{font-size:20px;letter-spacing:2px;color:var(--ink);font-weight:600;margin-bottom:12px}
.enquiry-grid{display:grid;grid-template-columns:1fr 1fr 1fr;gap:8px}
.enquiry-grid div{height:24px;background:#fff;border:1px solid var(--line);font-size:10px;color:var(--muted);padding:5px 8px}
.enquiry-grid .note{background:none;border:0}
.enquiry-grid .send{background:var(--orange);border:0;color:#fff;font-family:"Oswald",sans-serif;letter-spacing:1px;text-align:center;font-size:10px}
.bottom-bar{position:absolute;top:2226px;left:0;width:1200px;height:30px;background:var(--night);display:flex;align-items:center;justify-content:space-between;padding:0 180px;font-size:9px;color:#9a9da2}
</style>
</head>
<body>

<header class="site-header">
  <div class="brand"><span class="brand-dot"></span>Vault Learning</div>
  <nav class="nav">
    <a href="#" class="active">Home</a>
    <a href="#">About Us</a>
    <a href="#">Our Programs &amp; Shows</a>
    <a href="#">Teachers</a>
  </nav>
  <a href="#" class="btn">Book Now</a>
</header>

<section class="hero">
  <div class="hero-shelf photo" role="img" aria-label="Library bookshelves in warm light"></div>
  <div class="hero-stage photo" role="img" aria-label="Acrobat performing a leap on a dark stage"></div>
  <div class="hero-copy">
    <h1><em>Hello,</em> We're<br>Vault Learning</h1>
    <p>Acrobatic educational shows that bring big lessons to school halls.</p>
    <a href="#" class="btn">Book Now</a>
  </div>
  <div class="hero-phone">
    <svg width="12" height="12" viewBox="0 0 24 24"><path fill="#f5a623" d="M6.6 10.8a15.1 15.1 0 006.6 6.6l2.2-2.2a1 1 0 011-.25 11.4 11.4 0 003.6.57 1 1 0 011 1V20a1 1 0 01-1 1A17 17 0 013 4a1 1 0 011-1h3.5a1 1 0 011 1 11.4 11.4 0 00.57 3.6 1 1 0 01-.25 1z"/></svg>
    (03) 5550 1842
  </div>
  <div class="slider-dots"><span>&#8592;</span><span>&#8594;</span></div>
</section>

<section class="feature">
  <div class="feature-photo photo" role="img" aria-label="Young gymnast stretching on a studio floor"></div>
  <div class="feature-copy">
    <h2>Kindness-First<br>Tumbling Tour</h2>
    <h3>Educating the Victim, Empowering the Bystander, and Enlightening the Bully</h3>
    <p>A high-energy live show that uses parkour and acrobatics to open honest conversations about bullying, friendship and standing up for one another.</p>
    <div class="feature-rule"></div>
  </div>
</section>

<section class="programs">
  <h4>OUR PROGRAMS &amp; SHOWS</h4>
  <div class="arrows">&#8592;&#8594;</div>
  <div class="cards">
    <div class="card"><div class="photo" role="img" aria-label="Students watching a show in a school hall" style="background:linear-gradient(160deg,#9fb0a0,#5d6c63)"></div><span>Primary Schools</span></div>
    <div class="card"><div class="photo" role="img" aria-label="Performers running along a city street" style="background:linear-gradient(160deg,#b9b6c4,#6b6878)"></div><span>Parkour Skills</span></div>
    <div class="card"><div class="photo" role="img" aria-label="Acrobat mid-flip in dark studio" style="background:linear-gradient(160deg,#6e4a3c,#241a17)"></div><span>Stage Shows</span></div>
    <div class="card"><div class="photo" role="img" aria-label="Teacher with a group of children" style="background:linear-gradient(160deg,#a9c3d8,#5f7e98)"></div><span>Teacher Resources</span></div>
  </div>
</section>

<section class="quote">
  <p>"Vault Learning engages children in important topics, by utilising Parkour &amp; Acrobatics to captivate and enthrall todays youngest generation."</p>
</section>

<section class="heroes">
  <div class="heroes-photo photo" role="img" aria-label="Performer balancing on one leg against a blue wall"></div>
  <div class="heroes-nav">&#8592; &#8594;</div>
  <div class="heroes-copy">
    <h2>Our Heros &amp; Programs</h2>
    <div class="name">Marisol Keane</div>
    <p class="intro">Lead performer and trained coach who turns every flip and vault into a moment children remember long after the show.</p>
    <div class="info-box">
      <h5>Favourite Subjects</h5>
      <p>Health and physical education, drama, science of motion and balance.</p>
      <h5>Skills</h5>
      <p>Parkour · Tumbling · Choreography · Storytelling</p>
      <h5>Programs</h5>
      <p>5 Shows</p>
    </div>
    <a href="#" class="btn">Read More About Our Heros</a>
  </div>
</section>

<section class="how">
  <div class="how-kid photo" role="img" aria-label="Smiling child jumping with arms raised"></div>
  <h2>HOW WE THINK AND WORK</h2>
  <p class="lead">Curriculum based resources for teachers including lesson plans, workbooks, and physical activities for before &amp; after the show.</p>
  <ul>
    <li>Fun &amp; Interactive</li>
    <li>Mathematics Links</li>
    <li>Science Activities</li>
    <li>Lesson Plans Provided</li>
    <li>PD/H/PE Workbooks</li>
    <li>Strong Positive Messages</li>
  </ul>
</section>

<section class="newsletter">
  <div class="field">
    <svg width="12" height="10" viewBox="0 0 24 18"><rect x="1" y="1" width="22" height="16" fill="none" stroke="#8a8d93" stroke-width="2"/><path d="M1 1l11 9 11-9" fill="none" stroke="#8a8d93" stroke-width="2"/></svg>
    Subscribe to our newsletter
  </div>
  <a href="#" class="btn">Subscribe</a>
</section>

<footer class="site-footer">
  <div class="footer-about">
    <div class="brand"><span class="brand-dot"></span>Vault Learning</div>
    <p>Live acrobatic shows and classroom resources for schools.<br>hello@vaultlearning.example · (03) 5550 1842</p>
    <div class="socials"><span></span><span></span><span></span><span></span><span></span><span></span></div>
  </div>
  <div class="enquiry">
    <h3>QUICK ENQUIRY</h3>
    <div class="enquiry-grid">
      <div>Your Name</div><div>Phone Number</div><div class="note">Get in touch</div>
      <div>Email Address</div><div>Your Message</div><div class="send">SEND MESSAGE</div>
    </div>
  </div>
</footer>

<div class="bottom-bar">
  <span>© Vault Learning. All rights reserved.</span>
  <span>Home · About · Contact</span>
</div>

</body>
</html>
```